Label or packaging Design for Hair Care Line

Dear Designer,
We are Corvella, a brand known for our premium hairstyling tools, and we are excited to expand into hair care. We are currently looking for a talented designer to create the label designs for our entire luxury hair care line.
This project is crucial in establishing our visual identity in the hair care market, and we aim to position ourselves alongside premium brands such as PLX, Varnette Coif Atelier, and Trevo.
Project Scope
We need a cohesive label design for our hair care line, which includes:
5 products (e.g., shampoo, conditioner, hair oil, styling cream, and a hair mask).
The designs should include:
Front label: Highlighting the product name, key features, and branding.
Our goal is to achieve a design that communicates premium luxury with a touch of professionalism. Below are the specific guidelines to help you align with our vision:
Style and Inspiration
Think of brands like PLX, Varnette Coif Atelier, and Trevo.
Luxury and Minimalism: Clean lines, sophisticated typography, and an elegant color palette.
Subtle femininity: premium finishes like metallic accents (gold, silver, or rose gold).
Brand Personality
Premium: Reflecting high quality and exclusivity.
Modern & Professional: Appealing to a refined, professional audience but also suitable for lifestyle-oriented customers.
Warm & Empowering: A brand that celebrates confidence and individuality.
Color Palette
Neutral tones like black, white, accented with metallics (gold or silver) for a luxurious feel.
Colors that feel timeless and elegant rather than trendy or overly bright.
Typography
Use clean, modern fonts (preferably sans-serif or serif for a refined look).
Clear and legible for all product details while maintaining a high-end aesthetic.
Materials and Finishes
Packaging Shape
The label designs should suit a variety of bottle and jar shapes (e.g., cylindrical, flat, or rounded).
Keep scalability in mind so the identity remains consistent across different products.
Deliverables
To understand the aesthetic we are aiming for, here are some brands to use as inspiration:
PLX: For its minimalistic and modern approach.
Varnette Coif Atelier: For its combination of luxury and professional appeal.
Trevo: For its soft femininity and lifestyle branding.
we would like to see your designs applied to a variety of packaging types to get an overall impression of how the brand identity works across different product formats. This includes:
A squeeze bottle (e.g., for styling creams or conditioners).
A glass bottle with a dropper (e.g., for a luxurious hair oil).
A shampoo/conditioner bottle (standard pump or flip-top cap).
A spray bottle (e.g., for leave-in treatments or heat protectors).
By creating designs for these different packaging types, we can better evaluate how cohesive and versatile the brand identity will be across the entire product line.

Updates
As you may have noticed from the designs, they don’t quite align with our briefing. The look needs to be clean and professional, similar to Varnette, PLX, and the other examples we provided. Please address this, and we’ll check it!

Target Market(s)
europe and us
Font styles to use
Other font styles liked:
- century gothic

Look and feel
Each slider illustrates characteristics of the customer's brand and the style your logo design should communicate.

```html
<!DOCTYPE html>
<html lang="en">
<head>
<meta charset="utf-8">
<title>Corvella Hair Care Labels</title>
<link href="https://fonts.googleapis.com/css2?family=Montserrat:wght@400;600;700&display=swap" rel="stylesheet">
<style>
  :root {
    --navy: #1c2142;
    --navy-soft: #262c52;
    --gold: #c8ad8b;
    --gold-deep: #b59878;
    --backdrop: #eceff4;
  }
  * { box-sizing: border-box; margin: 0; padding: 0; }
  html, body { width: 1200px; height: 900px; overflow: hidden; }
  body {
    background: var(--backdrop);
    font-family: "Montserrat", sans-serif;
    position: relative;
  }
  .label {
    position: absolute;
    background: var(--navy);
    overflow: hidden;
  }
  .label--tall { width: 320px; height: 440px; top: 230px; }
  .label--conditioner { left: 90px; }
  .label--styling { left: 790px; }
  .label--jar { width: 300px; height: 200px; left: 450px; top: 350px; }

  .floral-field {
    position: absolute; left: 0; top: 0; width: 100%;
    background: linear-gradient(180deg, var(--navy-soft), var(--navy));
  }
  .label--tall .floral-field { height: 215px; }
  .label--jar .floral-field { height: 80px; }

  .gold-rule {
    position: absolute; left: 0; width: 100%; height: 3px;
    background: var(--gold);
  }
  .label--tall .gold-rule--upper { top: 215px; }
  .label--tall .gold-rule--lower { top: 400px; }
  .label--jar .gold-rule--upper { top: 80px; }
  .label--jar .gold-rule--lower { top: 176px; }

  .brand-box {
    position: absolute; left: 50%; transform: translateX(-50%);
    background: var(--gold);
    box-shadow: 0 0 0 3px var(--navy), 0 0 0 5px var(--gold);
    display: flex; align-items: center; justify-content: center;
    color: var(--navy);
    font-weight: 400;
  }
  .label--tall .brand-box { top: 178px; width: 128px; height: 72px; font-size: 19px; }
  .label--jar .brand-box { top: 58px; width: 84px; height: 44px; font-size: 12px; }

  .product-name {
    position: absolute; left: 0; width: 100%; text-align: center;
    color: var(--gold); font-weight: 700; letter-spacing: 0.04em;
    text-transform: uppercase;
  }
  .label--tall .product-name { top: 285px; font-size: 20px; }
  .label--jar .product-name { top: 130px; font-size: 12px; }

  .product-copy {
    position: absolute; left: 60px; right: 60px; top: 335px;
    color: var(--gold); font-size: 7.5px; line-height: 1.45;
    text-align: center;
  }
</style>
</head>
<body>

  <section class="label label--tall label--conditioner">
    <div class="floral-field" role="img" aria-label="Fine gold line-drawn floral and leaf pattern on navy"></div>
    <div class="gold-rule gold-rule--upper"></div>
    <div class="brand-box">Corvella</div>
    <h2 class="product-name">Conditioner</h2>
    <p class="product-copy">Silk protein formula restores softness and shine to every strand. Apply to damp lengths after washing, leave for two minutes, then rinse thoroughly with warm water.</p>
    <div class="gold-rule gold-rule--lower"></div>
  </section>

  <section class="label label--jar">
    <div class="floral-field" role="img" aria-label="Fine gold line-drawn floral and leaf pattern on navy"></div>
    <div class="gold-rule gold-rule--upper"></div>
    <div class="brand-box">Corvella</div>
    <h2 class="product-name">Hair Mask</h2>
    <div class="gold-rule gold-rule--lower"></div>
  </section>

  <section class="label label--tall label--styling">
    <div class="floral-field" role="img" aria-label="Fine gold line-drawn floral and leaf pattern on navy"></div>
    <div class="gold-rule gold-rule--upper"></div>
    <div class="brand-box">Corvella</div>
    <h2 class="product-name">Styling Cream</h2>
    <p class="product-copy">Light hold cream that defines shape and tames frizz with a soft finish. Work a small amount through dry or damp hair and style as desired.</p>
    <div class="gold-rule gold-rule--lower"></div>
  </section>

</body>
</html>
```